Cap supplier needs a newsletter design design

Looking for a new/fresh idea for an e-mail news letter.
My current newsletter can be found at the link below.
http://rolnahats.com/newsletter_jan_2014/1a/index.html

The information needed does not change form the current newsletter.
Looking for a creative presentation with or without flash.

Industry/Entity Type

News

```html
<!DOCTYPE html>
<html lang="en">
<head>
<meta charset="utf-8">
<title>Rolna Bay International – Newsletter</title>
<link rel="stylesheet" href="https://fonts.googleapis.com/css2?family=Oswald:wght@400;500;600&family=Open+Sans:wght@400&display=swap">
<style>
:root{
  --page:#cfdbe3;
  --navy-dark:#1c1f2b;
  --navy:#112a63;
  --sky:#1fa9e6;
  --ink:#ffffff;
  --muted:#8c8f96;
  --link:#2a7fc0;
  --deep-title:#1a2b66;
  --mid-title:#2a3d8c;
}
*{margin:0;padding:0;box-sizing:border-box}
html,body{width:819px;height:1200px;overflow:hidden;background:var(--page)}
body{position:relative;font-family:'Oswald',sans-serif;color:var(--ink)}
.util{position:absolute;right:110px;font-family:'Open Sans',sans-serif;font-size:8.5px;color:var(--muted)}
.util a{color:var(--link);text-decoration:none;margin-left:5px}
.util-top{top:49px}
.util-bottom{top:1129px}
.newsletter{position:absolute;left:102px;top:65px;width:616px;height:1062px;background:#fff}
.band{background:linear-gradient(180deg,var(--navy-dark) 0%,var(--navy) 100%)}
.masthead{height:95px;text-align:center;padding-top:12px}
.masthead h1{font-weight:500;font-size:44px;line-height:46px;letter-spacing:.3px}
.masthead p{font-size:15px;line-height:18px;font-weight:500}
.hero{position:relative;height:397px;background:#fff}
.hero-photo{position:absolute;left:26px;top:4px;width:572px;height:385px;border-radius:30px;
  background:radial-gradient(ellipse at center,#ffffff 32%,#d7dbe6 60%,#2c3550 100%)}
.hero-title{position:absolute;left:200px;top:130px;width:250px;text-align:center;line-height:1}
.hero-title .l1{display:block;font-size:40px;color:var(--deep-title);font-weight:500;letter-spacing:1px}
.hero-title .l2{display:block;margin-top:2px}
.hero-title .small{font-size:19px;color:#8a8a8a;vertical-align:middle}
.hero-title .big{font-size:52px;color:var(--sky);vertical-align:middle}
.hero-title .l3{display:block;font-size:36px;color:var(--mid-title);font-weight:500;margin-left:-6px}
.video{position:relative;height:98px;text-align:center;padding-top:18px}
.video h2{font-size:36px;line-height:38px;font-weight:500;margin-left:-110px}
.video p{font-size:14px;line-height:18px;font-weight:500;margin-left:-108px}
.video svg{position:absolute;right:28px;top:7px}
.programs{position:relative;height:228px}
.program{position:absolute;top:22px;width:184px;height:188px;border-radius:16px;overflow:hidden;
  background:linear-gradient(180deg,#16303f 0%,#141c36 30%,#102a66 100%);box-shadow:0 1px 4px rgba(0,0,0,.35)}
.program header{height:62px;text-align:center;background:linear-gradient(180deg,#2d6a86 0%,#1a3344 100%);line-height:25px;padding-top:5px}
.program .kind{display:block;color:var(--sky);font-size:24px}
.program .word{display:block;font-size:24px;font-weight:500}
.program ul{list-style:none;padding:3px 0 0 34px;font-size:15px;line-height:18px}
.program li{margin-bottom:18px}
.p1{left:12px}.p2{left:216px}.p3{left:420px}
.p1 .kind,.p3 .kind{letter-spacing:.2px}
.contact{position:relative;height:244px;overflow:hidden}
.contact-photo{position:absolute;left:300px;top:-6px;width:316px;height:250px;border-radius:50% 40% 0 50%;
  background:radial-gradient(ellipse at 45% 45%,#d99a3a 0%,#9a5a22 30%,#15131a 65%,rgba(17,42,99,0) 80%)}
.contact .lead{position:absolute;left:12px;top:12px;font-size:15px;font-weight:500}
.contact .site{position:absolute;left:12px;top:26px;font-size:56px;line-height:66px;color:var(--sky);font-weight:500;letter-spacing:-.5px}
.contact address{position:absolute;left:14px;top:90px;font-style:normal;font-size:18px;line-height:22px;color:#a9b0c4;font-weight:500}
.contact .phone{position:absolute;left:14px;top:198px;font-size:12px;font-weight:500}
.contact .mail{position:absolute;left:14px;top:214px;font-size:12px;color:var(--sky);font-weight:500}
</style>
</head>
<body>
<div class="util util-top">Can't see te images below? <a href="http://rolnahats.com/newsletter_jan_2014/1a/index.html">Click Here</a></div>

<main class="newsletter">
  <header class="masthead band">
    <h1>ROLNA BAY INTERNATIONAL</h1>
    <p>IMPORTED CUSTOM HEADWEAR asi 40812</p>
  </header>

  <section class="hero">
    <div class="hero-photo" role="img" aria-label="Collage of twelve embroidered custom baseball caps in camo, royal blue, black and navy"></div>
    <div class="hero-title">
      <span class="l1">DESIGN A CAP</span>
      <span class="l2"><span class="small">WHICH IS </span><span class="big">UNIQUELY</span></span>
      <span class="l3">YOURS !</span>
    </div>
  </section>

  <section class="video band">
    <h2>WATCH HOW AMAZINGLY EASY IT IS</h2>
    <p>SEE THE SHORT VIDEO PRESENTATION EXPLAINING OUR SERVICE</p>
    <svg width="84" height="84" viewBox="0 0 84 84" aria-label="Play video">
      <defs><linearGradient id="playFill" x1="0" y1="0" x2="0" y2="1"><stop offset="0" stop-color="#5a6a8e"/><stop offset="1" stop-color="#1d2d5c"/></linearGradient></defs>
      <circle cx="42" cy="42" r="38" fill="url(#playFill)" stroke="#fff" stroke-width="5"/>
      <path d="M33 25 L60 42 L33 59 Z" fill="#fff"/>
    </svg>
  </section>

  <section class="programs">
    <article class="program p1">
      <header><span class="kind">CUSTOM</span><span class="word">PROGRAM</span></header>
      <ul><li>Design a cap which is uniquely yours</li><li>150 cap minimum</li><li>40-50 day delivery</li></ul>
    </article>
    <article class="program p2">
      <header><span class="kind">STANDARD</span><span class="word">PROGRAM</span></header>
      <ul><li>Custom , but the options are limited</li><li>150 cap minimum</li><li>40-50 day delivery</li></ul>
    </article>
    <article class="program p3">
      <header><span class="kind">KNIT HAT &amp; SCARF</span><span class="word">PROGRAM</span></header>
      <ul><li>Winter items with custom creativity</li><li>150 cap minimum</li><li>40-50 day delivery</li></ul>
    </article>
  </section>

  <footer class="contact band">
    <div class="contact-photo" role="img" aria-label="Black cap with embroidered tiger design and paw prints"></div>
    <p class="lead">FOR MORE INFORMATION VISIT OUR WEBSITE</p>
    <p class="site">WWW.ROLNAHATS.COM</p>
    <address>ROLNA BAY INTERNATIONAL<br>1420 MAPLE CREST ROAD<br>FAIRVIEW,<br>VA,<br>22041</address>
    <p class="phone">TELEPHONE &nbsp;555-014-2273</p>
    <p class="mail">ROLNAHATS@MAILHOST.NET</p>
  </footer>
</main>

<div class="util util-bottom">Want to unsubscribe from this newsletter ? <a href="#">Click Here</a></div>
</body>
</html>
```